Website Design for Law Firm

We need a fresh new website design for our client 'Torvek Legal' who specialises as a Criminal, Traffic & Civil Lawyer in Perth, Western Australia. We are looking for a very clean, professional and elegant look for the website, a presence of power and class needed as he deals with high end clients. Black, Silver and hints of gold need to run through the design without making the site look too dark. We are after a very modern, spacious web look, use of large readable text with links to social media (such as Kindra, Google+, Peeplet, Worklinq) to stand out and his contact details to be made very predominate.

Reason: Public holidays here in Australia, need more business hours to discuss designs with client.

Reason: Client needs more time to look through designs.

Reason: Client is going over last of designs. Design will be picked early next week!

Law Firm

```html
<!DOCTYPE html>
<html lang="en">
<head>
<meta charset="utf-8">
<title>Torvek Legal — Defence Lawyer Perth</title>
<link rel="stylesheet" href="https://fonts.googleapis.com/css2?family=Libre+Baskerville:wght@400;700&family=Raleway:wght@400;500;600&display=swap">
<style>
:root{
  --ink:#2b2b2b;
  --dark:#2e2e2e;
  --darker:#232323;
  --gold:#c9974f;
  --news:#b07a32;
  --muted:#7d8a96;
  --line:#d6d6d6;
  --page:#fafbfb;
  --serif:'Libre Baskerville',Georgia,serif;
  --sans:'Raleway',Arial,sans-serif;
}
*{margin:0;padding:0;box-sizing:border-box}
html,body{width:956px;height:1200px;overflow:hidden}
body{background:var(--page);font-family:var(--sans);color:var(--ink);position:relative}

/* header */
.site-header{position:absolute;top:0;left:0;width:956px;height:112px;background:linear-gradient(#f7f7f7,#efefef)}
.brand{position:absolute;left:127px;top:28px;display:flex;align-items:center;gap:8px;font-family:var(--serif);font-weight:700;font-size:25px;color:var(--darker);letter-spacing:.5px}
.brand-mark{width:14px;height:14px;background:var(--darker)}
.social-top{position:absolute;right:118px;top:15px;display:flex;gap:11px}
.social-box{width:24px;height:24px;background:var(--darker);color:#fff;font:600 11px var(--sans);display:flex;align-items:center;justify-content:center}
.assess{position:absolute;right:118px;top:54px;font-size:10px;display:flex;align-items:center;gap:5px}
.assess b{font-weight:700}
.call{position:absolute;right:118px;top:68px;font-family:var(--serif);font-size:20px;color:var(--gold)}

/* nav */
.main-nav{position:absolute;top:112px;left:0;width:956px;height:33px;background:linear-gradient(#4a4a4a,#2a2a2a);display:flex;justify-content:center}
.main-nav ul{list-style:none;display:flex;gap:18px;padding-left:8px;align-items:center}
.main-nav a{color:#fff;text-decoration:none;font-family:var(--serif);font-size:11px}

/* hero */
.hero{position:absolute;top:145px;left:0;width:956px;height:302px;background:linear-gradient(100deg,#fbfbfb 0%,#ececec 30%,#c4c7ca 52%,#6d7486 66%,#4a5168 76%,#9a9ea4 88%,#c8cacc 100%)}
.hero h1{position:absolute;left:134px;top:86px;font-family:var(--serif);font-weight:400;font-size:30px;line-height:34px;color:var(--ink)}
.hero p{position:absolute;left:134px;top:171px;font-size:12px;line-height:19px;color:#333}

/* lead band */
.lead{position:absolute;top:447px;left:0;width:956px;height:113px;background:linear-gradient(#3a3a3a,#2c2c2c)}
.lead h2{position:absolute;left:127px;top:17px;font-family:var(--serif);font-weight:400;font-size:14px;color:#fff}
.lead h2 .g{color:var(--gold)}
.field{position:absolute;background:#fff;border:1px solid #ccc;font-size:10px;color:#555;padding:5px 8px}
.btn{position:absolute;left:664px;top:46px;width:164px;height:48px;background:linear-gradient(#d7aa66,#b8853e);border-radius:3px;color:#fff;font-family:var(--serif);font-weight:700;font-size:14px;display:flex;align-items:center;justify-content:center}

/* services */
.services{position:absolute;top:592px;left:127px;width:703px;display:grid;grid-template-columns:239px 238px 226px;row-gap:21px}
.service{display:flex;align-items:center;gap:11px;font-family:var(--serif);font-size:13px}
.service-icon{flex-shrink:0;width:40px;height:40px;background:linear-gradient(135deg,#3a3a3a 50%,#222 50%);display:flex;align-items:center;justify-content:center}

/* columns */
.col{position:absolute;top:741px;width:224px}
.col h3{font-family:var(--serif);font-weight:400;font-size:14px;padding:0 1px 14px;border-bottom:3px double var(--line)}
.ph{margin-top:13px;width:224px;height:107px}
.welcome-text{margin-top:13px;font-size:9.5px;line-height:14px;color:var(--muted)}
.more{margin-top:10px;font-size:7px;letter-spacing:.5px;color:#555;display:flex;align-items:center;gap:5px}
.more:before{content:"";border-left:3px solid #666;border-top:2.5px solid transparent;border-bottom:2.5px solid transparent}
.contact-list{list-style:none;margin-top:12px;font-size:9px;color:#444}
.contact-list li{display:flex;gap:10px;margin-bottom:9px;line-height:15px}
.news{list-style:none;margin-top:13px}
.news li{display:flex;gap:8px;height:62px}
.date{flex-shrink:0;width:44px;height:44px;background:#a7a7a7;color:#fff;text-align:center;font-size:16px;padding-top:7px;line-height:16px}
.date small{display:block;font-size:7px;line-height:12px;white-space:nowrap}
.news-body{width:172px}
.news h4{font-family:var(--serif);font-size:10px;line-height:13px;color:var(--news);font-weight:700}
.news .more{margin-top:7px}

/* footer */
.site-footer{position:absolute;top:1013px;left:0;width:956px;height:151px;background:var(--dark)}
.foot-links{position:absolute;top:27px;list-style:none;font-size:9px;color:#bbb;letter-spacing:.3px}
.foot-links li{height:22.4px;display:flex;align-items:center;gap:6px}
.foot-links li:before{content:"";border-left:3px solid #555;border-top:2.5px solid transparent;border-bottom:2.5px solid transparent}
.pay-note{position:absolute;left:489px;top:26px;width:140px;font-size:9.5px;line-height:16px;color:#bbb}
.cards{position:absolute;left:487px;top:66px;display:flex;gap:10px}
.card{width:42px;height:27px;background:#fff;color:var(--darker);font:600 8px var(--sans);display:flex;align-items:center;justify-content:center}
.foot-contact{position:absolute;left:666px;top:26px;font-size:9.5px;line-height:16px;color:#bbb}
.foot-contact span{color:var(--gold)}
.social-foot{position:absolute;left:666px;top:66px;display:flex;gap:12px}
.social-foot .social-box{background:#fff;color:var(--darker)}
.bottom-bar{position:absolute;top:1164px;left:0;width:956px;height:36px;background:var(--darker);font-size:7.5px;color:#aaa}
.bottom-bar .copy{position:absolute;left:127px;top:14px}
.bottom-bar .legal{position:absolute;right:188px;top:14px}
</style>
</head>
<body>

<header class="site-header">
  <div class="brand"><span class="brand-mark"></span>Torvek Legal</div>
  <div class="social-top">
    <span class="social-box" aria-label="Kindra">K</span>
    <span class="social-box" aria-label="Peeplet">P</span>
    <span class="social-box" aria-label="Worklinq">W</span>
  </div>
  <div class="assess">
    <svg width="11" height="11" viewBox="0 0 24 24"><path fill="#222" d="M6.6 10.8a15 15 0 006.6 6.6l2.2-2.2a1 1 0 011-.25 11.4 11.4 0 003.6.57 1 1 0 011 1V20a1 1 0 01-1 1A17 17 0 013 4a1 1 0 011-1h3.5a1 1 0 011 1c0 1.25.2 2.45.57 3.57a1 1 0 01-.25 1z"/></svg>
    Obligation <b>FREE</b> case assessment
  </div>
  <div class="call">Call 0400 555 014</div>
</header>

<nav class="main-nav">
  <ul>
    <li><a href="#">Home</a></li><li><a href="#">About</a></li><li><a href="#">Practice Areas</a></li>
    <li><a href="#">Scope Of Advice</a></li><li><a href="#">Legal Costs</a></li><li><a href="#">Press</a></li>
    <li><a href="#">Recent Cases</a></li><li><a href="#">Faq</a></li><li><a href="#">Links</a></li>
    <li><a href="#">Contact</a></li><li><a href="#">Service Policy</a></li>
  </ul>
</nav>

<section class="hero" role="img" aria-label="Photo of a lawyer in a navy suit before a grey city skyline">
  <h1>Trusted &amp; Experienced<br>Defence Lawyer</h1>
  <p>Criminal Defence Lawyer, Traffic Defence Lawyer &amp;<br>Civil Litigation Lawyer, Perth WA</p>
</section>

<section class="lead">
  <h2><span class="g">Get Help Today.</span> Receive an obligation <span class="g">FREE</span> case assessment.</h2>
  <div class="field" style="left:127px;top:46px;width:283px;height:23px">Full Name</div>
  <div class="field" style="left:127px;top:71px;width:141px;height:23px">Email</div>
  <div class="field" style="left:271px;top:71px;width:139px;height:23px">Phone</div>
  <div class="field" style="left:425px;top:46px;width:224px;height:48px">Message</div>
  <div class="btn">Get Started</div>
</section>

<section class="services">
  <div class="service"><span class="service-icon"><svg width="22" height="14" viewBox="0 0 22 14"><circle cx="6" cy="8" r="4.5" fill="none" stroke="#fff" stroke-width="1.6"/><circle cx="16" cy="8" r="4.5" fill="none" stroke="#fff" stroke-width="1.6"/><path d="M9 4h4" stroke="#fff" stroke-width="1.6"/></svg></span>Criminal Defence Lawyer</div>
  <div class="service"><span class="service-icon"><svg width="22" height="14" viewBox="0 0 22 14"><path d="M2 7l3-6h12l3 6v5H2z" fill="#fff"/><circle cx="5.5" cy="9" r="1.3" fill="#333"/><circle cx="16.5" cy="9" r="1.3" fill="#333"/></svg></span>Traffic Defence Lawyer</div>
  <div class="service"><span class="service-icon"><svg width="22" height="20" viewBox="0 0 22 20"><path d="M11 1v17M4 4h14M7 19h8" stroke="#fff" stroke-width="1.6"/><path d="M1 11l3-7 3 7zM15 11l3-7 3 7z" fill="none" stroke="#fff" stroke-width="1.3"/></svg></span>Civil Litigation Lawyer</div>
  <div class="service"><span class="service-icon"><svg width="18" height="22" viewBox="0 0 18 22"><rect x="1" y="1" width="16" height="20" fill="#fff"/><path d="M4 8h10M4 11h10M4 14h10M4 17h7" stroke="#333" stroke-width="1.2"/><rect x="4" y="3" width="4" height="3" fill="#333"/></svg></span>Special Applications</div>
  <div class="service"><span class="service-icon"><svg width="22" height="20" viewBox="0 0 22 20"><path d="M3 5l6-4 3 4-6 4z" fill="#fff"/><path d="M9 6l10 10" stroke="#fff" stroke-width="2.2"/><rect x="2" y="16" width="10" height="3" fill="#fff"/></svg></span>Breaching Offenses</div>
  <div class="service"><span class="service-icon"><svg width="22" height="20" viewBox="0 0 22 20"><path d="M11 1L1 6h20z" fill="#fff"/><path d="M4 8v8M9 8v8M13 8v8M18 8v8" stroke="#fff" stroke-width="2"/><rect x="1" y="17" width="20" height="2" fill="#fff"/></svg></span>Court Work</div>
</section>

<section class="col" style="left:127px">
  <h3>Welcome To Torvek Legal</h3>
  <div class="ph" role="img" aria-label="Lawyers in suits in discussion" style="background:linear-gradient(120deg,#6a6e74,#2f3238 50%,#8d8f92)"></div>
  <p class="welcome-text">Torvek Legal is an established law firm practicing in Criminal Law, Traffic Law and Civil Law. We are conveniently located close to the Perth Magis-trates Court and District Court.</p>
  <div class="more">READ MORE</div>
</section>

<section class="col" style="left:365px">
  <h3>Contact Us</h3>
  <div class="ph" role="img" aria-label="Street map showing the office location" style="background:linear-gradient(135deg,#e4e2dc,#d8dcd0 50%,#c7d6e2)"></div>
  <ul class="contact-list">
    <li><svg width="12" height="12" viewBox="0 0 24 24"><path fill="#777" d="M6.6 10.8a15 15 0 006.6 6.6l2.2-2.2a1 1 0 011-.25 11.4 11.4 0 003.6.57 1 1 0 011 1V20a1 1 0 01-1 1A17 17 0 013 4a1 1 0 011-1h3.5a1 1 0 011 1c0 1.25.2 2.45.57 3.57a1 1 0 01-.25 1z"/></svg>+0400 555 014</li>
    <li><svg width="12" height="12" viewBox="0 0 24 24"><rect x="2" y="5" width="20" height="14" fill="none" stroke="#777" stroke-width="2"/><path d="M2 5l10 8 10-8" fill="none" stroke="#777" stroke-width="2"/></svg>info@yourwebsite.com</li>
    <li><svg width="12" height="14" viewBox="0 0 24 28"><path fill="#777" d="M12 0a9 9 0 00-9 9c0 7 9 19 9 19s9-12 9-19a9 9 0 00-9-9zm0 13a4 4 0 110-8 4 4 0 010 8z"/></svg>Your Address, Your Country<br>Your Zip Code</li>
  </ul>
</section>

<section class="col" style="left:605px">
  <h3>Latest News</h3>
  <ul class="news">
    <li><div class="date">05<small>May 2014</small></div><div class="news-body"><h4>Learner driver Darian Koss admits death crash charges</h4><div class="more">READ MORE</div></div></li>
    <li><div class="date">05<small>May 2014</small></div><div class="news-body"><h4>Waikiki teen jailed after armed robberies</h4><div class="more">READ MORE</div></div></li>
    <li><div class="date">05<small>May 2014</small></div><div class="news-body"><h4>Mentally ill man avoids jail for indecent dealings</h4><div class="more">READ MORE</div></div></li>
  </ul>
</section>

<footer class="site-footer">
  <ul class="foot-links" style="left:127px"><li>HOME</li><li>ABOUT US</li><li>PRACTICE AREAS</li><li>SCOPE OF ADVICE</li><li>LEGAL COSTS</li></ul>
  <ul class="foot-links" style="left:306px"><li>PRESS</li><li>RECENT CASES</li><li>FAQ</li><li>LINKS</li><li>SERVICE POLICY</li></ul>
  <p class="pay-note">For payment, we accept the following:</p>
  <div class="cards"><span class="card">Corvia</span><span class="card">Paylink</span><span class="card">Tapcard</span></div>
  <p class="foot-contact">Phone : <span>0400 555 014</span><br>Email : <span>info@torveklegal.example</span></p>
  <div class="social-foot">
    <span class="social-box" aria-label="Kindra">K</span>
    <span class="social-box" aria-label="Peeplet">P</span>
    <span class="social-box" aria-label="Worklinq">W</span>
  </div>
</footer>

<div class="bottom-bar">
  <span class="copy">Copyright © 2014. Torvek Legal. All Rights Reserved .</span>
  <span class="legal">Privacy Policy | Sitemap</span>
</div>

</body>
</html>
```